New Stationery Design Project

We got a project done from you for Pravonix stationary design. We have changed the name of the company from Pravonix to Kelmra.
So we want to redesign our stationay.
We are a VOIP, hosted pbx, and cloud services provider. Clients are mostly hotels, offices, business etc. needing phone services.
Our Slogan is : "Low cost, high quality service"
the logo has to be changed from Pravonix to Kelmra
Business address is
4172 Marrow Pkwy, suite 210
Dallas TX 75399
Phone: 555-013-4872
Fax: 555-013-4872
Website: Kelmra.example
Industry/Entity Type
Business
Look and feel
Each slider illustrates characteristics of the customer's brand and the style your logo design should communicate.

```html
<!DOCTYPE html>
<html lang="en">
<head>
<meta charset="utf-8">
<title>Kelmra Folder Covers</title>
<link href="https://fonts.googleapis.com/css2?family=Barlow:wght@400;500;600&display=swap" rel="stylesheet">
<style>
  :root {
    --backdrop: #b9b9b9;
    --paper: #f2f2f2;
    --cover-dark: #2b2b2b;
    --ink: #2a2a2a;
    --ink-soft: #555555;
    --accent-blue: #1aa3d9;
    --accent-pink: #d6197a;
    --accent-orange: #e0771d;
    --accent-red: #d8262c;
    --slogan: #d9d9d9;
  }
  * { box-sizing: border-box; margin: 0; padding: 0; }
  html, body { width: 1200px; height: 720px; overflow: hidden; }
  body {
    background: var(--backdrop);
    font-family: "Barlow", Arial, sans-serif;
    display: flex;
    align-items: center;
    justify-content: center;
    gap: 60px;
  }
  .cover {
    position: relative;
    width: 440px;
    height: 580px;
    box-shadow: 0 6px 18px rgba(0,0,0,0.25);
    overflow: hidden;
  }
  .cover--back { background: var(--paper); }
  .cover--front { background: var(--cover-dark); }

  .brand {
    display: flex;
    align-items: center;
    gap: 10px;
    font-weight: 600;
  }
  .brand__dot {
    width: 34px; height: 34px;
    border-radius: 50%;
    background: var(--accent-blue);
  }
  .cover--back .brand {
    position: absolute;
    top: 170px; left: 0; right: 0;
    justify-content: center;
    font-size: 34px;
    color: var(--ink);
  }
  .cover--front .brand {
    position: absolute;
    top: 150px; left: 0; right: 0;
    justify-content: center;
    font-size: 64px;
    color: #ffffff;
  }
  .cover--front .brand__dot { width: 58px; height: 58px; }

  .contact {
    position: absolute;
    top: 350px; left: 0; right: 0;
    text-align: center;
    font-size: 11px;
    font-weight: 500;
    line-height: 1.45;
    color: var(--ink-soft);
  }
  .contact__label { color: var(--accent-blue); margin-right: 4px; }
  .contact__address { margin-top: 12px; }
  .contact__web { margin-top: 16px; color: var(--accent-red); font-weight: 600; }

  .slogan-row {
    position: absolute;
    top: 360px; left: 0; right: 0;
    display: flex;
    align-items: center;
    gap: 14px;
  }
  .slogan-row__rule {
    flex: 1;
    height: 3px;
    background: var(--accent-blue);
  }
  .slogan {
    font-size: 17px;
    letter-spacing: 0.5px;
    color: var(--slogan);
    white-space: nowrap;
  }

  .bubble-band {
    position: absolute;
    left: 0; right: 0; bottom: 0;
    height: 22px;
    background: linear-gradient(90deg,
      var(--accent-blue) 0%, var(--accent-orange) 18%, var(--accent-blue) 36%,
      var(--accent-pink) 55%, var(--accent-orange) 78%, var(--accent-red) 100%);
  }
</style>
</head>
<body>
  <section class="cover cover--back" aria-label="Folder back cover">
    <div class="brand"><span class="brand__dot"></span><span class="brand__name">Kelmra</span></div>
    <div class="contact">
      <p><span class="contact__label">T</span>555-013-4872</p>
      <p><span class="contact__label">F</span>555-013-4872</p>
      <p class="contact__address">4172 Marrow Pkwy, suite 210<br>Dallas TX 75399</p>
      <p class="contact__web">Kelmra.example</p>
    </div>
    <div class="bubble-band" role="img" aria-label="Band of colourful speech bubbles"></div>
  </section>

  <section class="cover cover--front" aria-label="Folder front cover">
    <div class="brand"><span class="brand__dot"></span><span class="brand__name">Kelmra</span></div>
    <div class="slogan-row">
      <span class="slogan-row__rule"></span>
      <p class="slogan">Low cost, high quality service</p>
      <span class="slogan-row__rule"></span>
    </div>
    <div class="bubble-band" role="img" aria-label="Band of colourful speech bubbles"></div>
  </section>
</body>
</html>
```